Create look and feel for existing Web Page

Update Web Page

We have a website at http://www.usekivra.com/index-web.html. It is a single page html site, with a custom signup form. We also have a quill bay plugin at the bottom of the page. We'd like to redesign the look and feel of the entire site. We sell software to eye doctors. Also called optometrists, our software tool makes it easy for doctors to manage patients, bill, and document patient encounters. I have included our logos below.

We are looking for a new design preferably in HTML 5, CSS etc. The fields on the form on this page: http://www.usekivra.com/index-web.html

You can get screen shots of our software application at this site: http://staging.usekivra.com
username: test@samplevora.com
password: password

```html
<!DOCTYPE html>
<html lang="en">
<head>
<meta charset="utf-8">
<title>ocvela — The Practice Operating System</title>
<link href="https://fonts.googleapis.com/css2?family=Ubuntu:wght@300;400;500;700&family=Roboto:wght@300;400&display=swap" rel="stylesheet">
<style>
:root{
  --orange:#ff8416;
  --teal:#1fa4b8;
  --teal-deep:#12889c;
  --ink:#2b2b2b;
  --text:#555;
  --muted:#8a8a8a;
  --line:#e4e4e4;
  --white:#fff;
  --footer:#2c2c2c;
  --partners:#efefef;
}
*{box-sizing:border-box;margin:0;padding:0}
html,body{width:1200px;height:3062px;overflow:hidden}
body{font-family:"Ubuntu",sans-serif;color:var(--text);background:var(--white);position:relative}
.site-header{height:76px;display:flex;align-items:center;justify-content:space-between;padding:0 140px 0 122px}
.brand{font-size:38px;font-weight:400;color:var(--orange);letter-spacing:2px}
.main-nav{display:flex;gap:15px;font-size:14px}
.main-nav a{color:#777;text-decoration:none}
.main-nav a.active{color:var(--orange)}

.hero{position:relative;height:541px;background:radial-gradient(ellipse at 30% 60%,#3cc6d6 0%,var(--teal) 45%,var(--teal-deep) 100%)}
.hero-copy{position:absolute;left:91px;top:72px;width:560px;color:var(--white)}
.hero-title{font-size:32px;font-weight:700;color:var(--orange);line-height:37px;text-transform:uppercase}
.hero-lead{font-size:14px;line-height:21px;margin-top:20px}
.hero-tag{font-size:14px;margin-top:18px}
.hero-points{font-size:13.5px;margin-top:18px;letter-spacing:.3px}
.btn-light{display:inline-block;margin-top:30px;background:var(--white);color:#555;border-radius:22px;padding:12px 22px;font-size:14px}
.signup-card{position:absolute;left:679px;top:70px;width:393px;height:400px;background:var(--white);padding:34px 36px}
.signup-card h2{font-size:15.5px;font-weight:500;color:var(--orange);text-align:center;line-height:19px;text-transform:uppercase}
.field{height:33px;border:1px solid var(--line);margin-top:14px;padding:0 11px;font-size:13.5px;color:#666;display:flex;align-items:center}
.signup-card .field:first-of-type{margin-top:16px}
.btn-orange{display:block;width:230px;margin:18px auto 0;background:var(--orange);color:var(--white);border-radius:22px;padding:12px 0;text-align:center;font-size:14px}

.features{height:851px;padding-top:38px;text-align:center}
.features h2{font-size:31px;font-weight:400;color:var(--orange)}
.features .sub{font-size:10px;color:#444;margin-top:8px}
.feature-grid{display:grid;grid-template-columns:repeat(3,336px);row-gap:50px;margin:118px 0 0 82px;text-align:left}
.feature{position:relative;padding-left:27px;height:162px}
.feature .kicker{font-size:9.5px;color:var(--muted);font-family:"Roboto",sans-serif;font-weight:300}
.feature svg{display:block;margin-top:12px;width:27px;height:27px}
.feature h3{font-family:"Roboto",sans-serif;font-weight:300;font-size:20px;color:var(--ink);margin-top:5px;position:relative}
.feature h3::before{content:"";position:absolute;left:-27px;top:12px;width:17px;height:2px;background:var(--orange)}
.feature p{font-family:"Roboto",sans-serif;font-weight:300;font-size:9.5px;line-height:16px;color:var(--muted);margin-top:6px;width:280px}

.pricing{height:701px;background:linear-gradient(135deg,#e8ece9 0%,#dbe9ee 40%,#ece7e0 70%,#d4e6ee 100%);padding:35px 0 0 92px}
.price-grid{display:grid;grid-template-columns:repeat(3,307px);column-gap:28px;row-gap:15px}
.price-card{background:var(--white);height:300px;border:1px solid #e3e3e3;padding:0 14px;text-align:center}
.price-card h4{font-size:13px;font-weight:400;color:#333;height:62px;line-height:74px;border-bottom:1px solid #ddd}
.price{display:flex;justify-content:center;align-items:flex-start;height:68px;padding-top:12px;color:var(--orange)}
.price .amount{font-size:52px;font-weight:700;line-height:54px}
.price .cur{font-size:26px;font-weight:700;margin-left:8px;line-height:26px}
.price .per{font-size:8px;color:#666;align-self:flex-end;margin:0 0 10px -12px}
.per-loc{font-size:14px;color:#777;border-bottom:1px solid #ddd;padding-bottom:4px}
.price-card p{font-size:13.5px;color:#333;line-height:21px;margin-top:14px;height:44px}
.btn-outline{display:inline-block;margin-top:22px;border:1px solid var(--orange);color:var(--orange);border-radius:22px;padding:11px 20px;font-size:14px}

.cta-band{height:114px;background:var(--orange);display:flex;align-items:center;justify-content:space-between;padding:0 218px 0 200px}
.cta-band h3{font-weight:400;font-size:25px;color:var(--white)}
.cta-band .btn-light{margin:0;padding:12px 20px}

.testimonial{height:309px;text-align:center;padding-top:54px}
.avatar{width:88px;height:88px;border-radius:50%;margin:0 auto;border:2px solid var(--orange);background:linear-gradient(180deg,#c9d8e3,#8fa3b3)}
.testimonial blockquote{font-size:15.5px;line-height:24px;color:#555;width:800px;margin:25px auto 0}
.dots{display:flex;justify-content:center;gap:6px;margin-top:26px}
.dots span{width:8px;height:8px;border-radius:50%;background:#aaa}
.dots span.on{background:#222}

.partners{height:231px;background:var(--partners);text-align:center;padding-top:48px}
.partners h3{font-size:25px;font-weight:300;color:#555}
.partner-row{display:flex;justify-content:space-around;padding:0 120px;margin-top:38px}
.badge{width:96px;height:56px;background:#8c8c8c;border-radius:6px}
.badge.round{border-radius:50%;width:62px;height:62px}
.badge.wide{width:124px;height:40px;border-radius:20px;margin-top:8px}

.site-footer{height:239px;background:var(--footer);text-align:center;padding-top:44px}
.social{display:flex;justify-content:center;gap:24px}
.social span{width:14px;height:14px;border-radius:50%;background:#bbb}
.footer-nav{display:flex;justify-content:center;gap:14px;margin-top:40px;font-size:13.5px}
.footer-nav a{color:#ddd;text-decoration:none}
.newsletter{width:346px;height:32px;margin:38px auto 0;background:var(--white);border:1px solid #ccc;display:flex;align-items:center;justify-content:space-between;padding:0 10px;font-size:13.5px;color:#666}
</style>
</head>
<body>
<header class="site-header">
  <div class="brand">ocvela</div>
  <nav class="main-nav">
    <a class="active" href="#">Home</a><a href="#">About</a><a href="#">Services</a><a href="#">Products</a><a href="#">Features</a><a href="#">Pricing</a><a href="#">Contact</a>
  </nav>
</header>

<section class="hero" role="img" aria-label="Teal background with falling colourful confetti">
  <div class="hero-copy">
    <h1 class="hero-title">Lease Practices: Choose How<br>You Spend Your Time</h1>
    <p class="hero-lead">Ocvela Is Your Office Operating System. Automate Your Painful Tasks, Keep Track Of Your Books, And Live A Little. Start With A FREE Charting Tool And Add More Products As You Grow.</p>
    <p class="hero-tag">Meet Ocvela, The Practice Operating System</p>
    <p class="hero-points">SIMPLE • FULLY AUTOMATED • PROFITABLE</p>
    <span class="btn-light">Get The Charting Tool For Free</span>
  </div>
  <form class="signup-card">
    <h2>Get Started With A Free Charting Tool</h2>
    <div class="field">Full Name</div>
    <div class="field">Email Address</div>
    <div class="field">Cell Phone</div>
    <div class="field">Office Name</div>
    <div class="field">NPI</div>
    <span class="btn-orange">Get The Free Charting Tool</span>
  </form>
</section>

<section class="features">
  <h2>AI to Automate Optometry Office Tasks</h2>
  <p class="sub">Ocvela uses AI, automation, robots, and other cool technology to streamline office work so you can do things you love</p>
  <div class="feature-grid">
    <div class="feature"><div class="kicker">On Time!</div>
      <svg viewBox="0 0 24 24"><circle cx="12" cy="12" r="10" fill="none" stroke="#222" stroke-width="2.6"/><path d="M12 6v6l-3 3" fill="none" stroke="#222" stroke-width="2.6"/></svg>
      <h3>SCHEDULE</h3><p>Meet your patients where they are. 24 hours 7 days a week with the online scheduler..</p></div>
    <div class="feature"><div class="kicker">Best Quality!</div>
      <svg viewBox="0 0 24 24"><circle cx="9" cy="14" r="6" fill="none" stroke="#222" stroke-width="3" stroke-dasharray="3 2"/><circle cx="9" cy="14" r="2" fill="#222"/><circle cx="18" cy="6" r="4" fill="none" stroke="#222" stroke-width="2.5" stroke-dasharray="2 1.5"/></svg>
      <h3>INTAKE</h3><p>Never print out another paper form. Your patients are now able to fill out and sign forms online..</p></div>
    <div class="feature"><div class="kicker">Mobile apps!</div>
      <svg viewBox="0 0 24 24"><rect x="2" y="5" width="16" height="16" rx="2" fill="none" stroke="#222" stroke-width="2.2"/><path d="M10 14l10-10 2 2-10 10h-2z" fill="#222"/></svg>
      <h3>CHART</h3><p>Start charting all patient findings for FREE. With features like auto population it files on your mobile phone..</p></div>
    <div class="feature"><div class="kicker">HQ offer!</div>
      <svg viewBox="0 0 24 24"><path d="M5 2h9l5 5v15H5z" fill="none" stroke="#222" stroke-width="2"/><path d="M8 11h8M8 14h8M8 17h8" stroke="#222" stroke-width="1.6"/></svg>
      <h3>BILL</h3><p>Don't waste your precious time or pay someone to bill insurance, let a bot do it for you..</p></div>
    <div class="feature"><div class="kicker">Upload!</div>
      <svg viewBox="0 0 24 24"><path d="M12 2l4 6h-8zM3 19l3-7 4 6zM21 19l-7 0 3-7z" fill="#222"/><path d="M7 10l-3 5M17 10l3 5M8 21h8" stroke="#222" stroke-width="2.4" fill="none"/></svg>
      <h3>ELIGIBLE</h3><p>Don't call or login into every insurance website to get patient eligibility and copays. Our bots do that too..</p></div>
    <div class="feature"><div class="kicker">Best Result!</div>
      <svg viewBox="0 0 24 24"><path d="M12 21L3 12a5 5 0 0 1 9-6 5 5 0 0 1 9 6z" fill="#222"/></svg>
      <h3>REVIEW</h3><p>Grow your patient base and improve your search results with the review solution.</p></div>
    <div class="feature"><div class="kicker">Best Result!</div>
      <svg viewBox="0 0 24 24"><rect x="2" y="5" width="20" height="14" rx="2" fill="none" stroke="#222" stroke-width="2"/><path d="M2 7l10 7 10-7" fill="none" stroke="#222" stroke-width="2"/></svg>
      <h3>POST</h3><p>Grow your patient base and improve your search results with the review solution.</p></div>
    <div class="feature"><div class="kicker">Best Result!</div>
      <svg viewBox="0 0 24 24"><ellipse cx="9" cy="9" rx="8" ry="6.5" fill="#222"/><ellipse cx="16" cy="15" rx="7" ry="5.5" fill="#222" stroke="#fff" stroke-width="1"/></svg>
      <h3>REMIND</h3><p>Grow your patient base and improve your search results with the review solution.</p></div>
    <div class="feature"><div class="kicker">Best Result!</div>
      <svg viewBox="0 0 24 24"><path d="M20 10A8 8 0 0 0 5 7M4 14a8 8 0 0 0 15 3" fill="none" stroke="#222" stroke-width="2.8"/><path d="M3 3v6h6zM21 21v-6h-6z" fill="#222"/></svg>
      <h3>RECALL</h3><p>Grow your patient base and improve your search results with the review solution.</p></div>
  </div>
</section>

<section class="pricing">
  <div class="price-grid">
    <div class="price-card"><h4>FREE</h4><div class="price"><span class="amount">0</span><span class="cur">$</span></div><div class="per-loc">No Strings Attached</div><p>Chart Patient Findings For FREE. Unlimited Users, Doctors, And Location.</p><span class="btn-outline">SIGN UP TODAY</span></div>
    <div class="price-card"><h4>PICK 1 ADD ON</h4><div class="price"><span class="amount">99</span><span class="cur">$</span><span class="per">/ Per Month</span></div><div class="per-loc">Per Location</div><p>Choose Between Schedule, Intake, Bill, Eligible, Or Review.</p><span class="btn-outline">SIGN UP TODAY</span></div>
    <div class="price-card"><h4>PICK 2 ADD-ONS</h4><div class="price"><span class="amount">189</span><span class="cur">$</span><span class="per">/ Per Month</span></div><div class="per-loc">Per Location</div><p>Choose Any Two Features Between Schedule, Intake, Bill, Eligible, And/or Review.</p><span class="btn-outline">SIGN UP TODAY</span></div>
    <div class="price-card"><h4>PICK 3 ADD-ONS</h4><div class="price"><span class="amount">279</span><span class="cur">$</span><span class="per">/ Per Month</span></div><div class="per-loc">Per Location</div><p>Choose Any Three Features Between Schedule, Intake, Bill, Eligible, And/or Review.</p><span class="btn-outline">SIGN UP TODAY</span></div>
    <div class="price-card"><h4>PICK 4 ADD-ONS</h4><div class="price"><span class="amount">369</span><span class="cur">$</span><span class="per">/ Per Month</span></div><div class="per-loc">Per Location</div><p>Choose Any Four Features Between Schedule, Intake, Bill, Eligible, And/or Review.</p><span class="btn-outline">SIGN UP TODAY</span></div>
    <div class="price-card"><h4>PICK ALL ADD-ONS</h4><div class="price"><span class="amount">459</span><span class="cur">$</span><span class="per">/ Per Month</span></div><div class="per-loc">Per Location</div><p>Get All Five Features: Schedule, Intake, Bill, Eligible, And/or Review.</p><span class="btn-outline">SIGN UP TODAY</span></div>
  </div>
</section>

<section class="cta-band">
  <h3>Now spend time outside the office!</h3>
  <span class="btn-light">Join The Club</span>
</section>

<section class="testimonial">
  <div class="avatar" role="img" aria-label="Portrait photo of a customer"></div>
  <blockquote>Lorem ipsum dolor sit amet, consectetur adipisicing elit. Quidem, veritatis nulla eum laudantium totam tempore optio doloremque laboriosam quas, quos eaque molestias odio aut eius animi. Impedit temporibus nisi accusamus.</blockquote>
  <div class="dots"><span></span><span></span><span class="on"></span><span></span><span></span></div>
</section>

<section class="partners">
  <h3>Look for our special partners</h3>
  <div class="partner-row">
    <div class="badge" role="img" aria-label="Partner badge"></div>
    <div class="badge wide" role="img" aria-label="Partner badge"></div>
    <div class="badge round" role="img" aria-label="Partner badge"></div>
    <div class="badge wide" role="img" aria-label="Partner badge"></div>
  </div>
</section>

<footer class="site-footer">
  <div class="social"><span></span><span></span><span></span></div>
  <nav class="footer-nav"><a href="#">Home</a><a href="#">About Us</a><a href="#">Services</a><a href="#">Products</a><a href="#">Feautures</a><a href="#">Pricing</a><a href="#">Contact</a></nav>
  <div class="newsletter"><span>E-mail</span>
    <svg width="22" height="16" viewBox="0 0 22 16"><rect x="1" y="1" width="20" height="14" rx="2" fill="none" stroke="#ff8416" stroke-width="1.6"/><path d="M1 2l10 7 10-7" fill="none" stroke="#ff8416" stroke-width="1.6"/></svg>
  </div>
</footer>
</body>
</html>
```